Tide Harbor Finance Business Cards

Looking for a business card for a new mortgage broking business. Name of the business is Tide Harbor Finance. Purpose of the business is to build trust and strong relationships with clients to then assist them with your mortgage lending needs. Most relationships within the business start off as an enquiry, and then can evolve into a 10+ year relationship, servicing clients from purchasing a new home to then upgrading for their family and even then assisting their children with their first home purchase. Business card should communicate financial security and trust.

Target Market(s)

Targeting professional clients who are looking to build a relationship with a knowledgeable mortgage professional

Industry/Entity Type

Finance - Home Loans

Contact Information for Business Card

Peter Colburn, Director, mobile: 0427 903186, email:peter@tideharborfinance.com.au, website: www.tideharborfinance.com.au

Font styles to use
Sans Serif

Requirements
Must have
• On the front: Must have company logo, contact details as above. On the back: slogan, 'Steady guidance, secure futures', plus listing services offered: home loans, investment loans, first home buyers, refinancing, car finance

```html
<!DOCTYPE html>
<html lang="en">
<head>
<meta charset="utf-8">
<title>Tide Harbor Finance Business Cards</title>
<link rel="stylesheet" href="https://fonts.googleapis.com/css2?family=Montserrat:wght@400;500;600;700&display=swap">
<style>
  :root {
    --navy: #0d2a5e;
    --navy-deep: #0a2250;
    --brand-blue: #1b4e86;
    --orange: #f5a11c;
    --white: #ffffff;
    --rule: rgba(255,255,255,0.45);
    --paper: #f7f7f5;
    --ink: #1c1c1c;
    --backdrop: #3a3a3a;
  }
  * { box-sizing: border-box; margin: 0; padding: 0; }
  html, body { width: 1200px; height: 800px; overflow: hidden; }
  body {
    background: var(--backdrop);
    font-family: "Montserrat", sans-serif;
    display: flex;
    align-items: center;
    justify-content: center;
    gap: 50px;
  }
  .card {
    width: 525px;
    height: 300px;
    border-radius: 16px;
    position: relative;
    overflow: hidden;
  }

  /* Front */
  .card-front {
    background: linear-gradient(135deg, var(--navy-deep), var(--navy));
    color: var(--white);
  }
  .front-brand {
    position: absolute;
    left: 32px; top: 34px;
    display: flex; align-items: center; gap: 14px;
  }
  .brand-mark {
    width: 46px; height: 46px;
    border: 3px solid var(--white);
    border-radius: 8px;
    flex: none;
  }
  .brand-name {
    font-weight: 600;
    font-size: 19px;
    line-height: 1.05;
    text-transform: uppercase;
    letter-spacing: 0.5px;
  }
  .front-person {
    position: absolute; left: 32px; top: 140px;
  }
  .person-name {
    color: var(--orange);
    font-weight: 700;
    font-size: 26px;
  }
  .person-title {
    font-size: 14px;
    margin-top: 4px;
  }
  .front-rule {
    position: absolute; left: 32px; right: 32px; top: 212px;
    height: 1px; background: var(--rule);
  }
  .contact-item {
    position: absolute;
    display: flex; align-items: center; gap: 7px;
    list-style: none;
    font-size: 12px;
    font-weight: 500;
    white-space: nowrap;
  }
  .contact-phone { left: 32px; top: 226px; font-size: 17px; font-weight: 600; }
  .contact-email { left: 32px; top: 256px; }
  .contact-web { right: 32px; top: 230px; }
  .icon { width: 14px; height: 14px; flex: none; }

  /* Back */
  .card-back {
    background: var(--paper);
    color: var(--brand-blue);
    display: flex; flex-direction: column; align-items: center;
    padding-top: 40px;
  }
  .back-brand { display: flex; align-items: center; gap: 14px; }
  .back-brand .brand-mark { border-color: var(--brand-blue); width: 50px; height: 50px; }
  .back-brand .brand-name { color: var(--brand-blue); font-size: 21px; }
  .slogan {
    margin-top: 30px;
    font-weight: 700;
    font-size: 21px;
    text-transform: uppercase;
    letter-spacing: 0.3px;
    white-space: nowrap;
  }
  .services-heading {
    margin-top: 16px;
    display: flex; align-items: center; gap: 10px;
    font-weight: 700; font-size: 19px; color: var(--ink);
  }
  .services-heading .accent { color: var(--orange); }
  .arrow { width: 12px; height: 12px; fill: var(--orange); }
  .services-list {
    margin-top: 14px;
    list-style: none;
    display: flex; flex-wrap: wrap; justify-content: center;
    max-width: 420px;
    row-gap: 6px;
    color: var(--ink);
    font-size: 13.5px;
  }
  .service { padding: 0 10px; border-left: 1.5px solid var(--brand-blue); }
  .service:first-child, .service.row-start { border-left: none; }
</style>
</head>
<body>
  <section class="card card-front" aria-label="Business card front">
    <div class="front-brand">
      <div class="brand-mark"></div>
      <div class="brand-name">Tide<br>Harbor<br>Finance</div>
    </div>
    <div class="front-person">
      <div class="person-name">Peter Colburn</div>
      <div class="person-title">Director</div>
    </div>
    <div class="front-rule"></div>
    <ul class="contact-list">
      <li class="contact-item contact-phone">
        <svg class="icon" viewBox="0 0 24 24"><path fill="#f5a11c" d="M6.6 10.8a15 15 0 0 0 6.6 6.6l2.2-2.2a1 1 0 0 1 1-.25 11.4 11.4 0 0 0 3.6.57 1 1 0 0 1 1 1V20a1 1 0 0 1-1 1A17 17 0 0 1 3 4a1 1 0 0 1 1-1h3.5a1 1 0 0 1 1 1c0 1.25.2 2.45.57 3.57a1 1 0 0 1-.25 1z"/></svg>
        0427 903186
      </li>
      <li class="contact-item contact-web">
        <svg class="icon" viewBox="0 0 24 24"><circle cx="12" cy="12" r="9" fill="none" stroke="#f5a11c" stroke-width="2"/><path d="M3 12h18M12 3c3 3 3 15 0 18M12 3c-3 3-3 15 0 18" fill="none" stroke="#f5a11c" stroke-width="1.6"/></svg>
        www.tideharborfinance.com.au
      </li>
      <li class="contact-item contact-email">
        <svg class="icon" viewBox="0 0 24 24"><path fill="#f5a11c" d="M2 11 22 3l-8 18-2.5-7.5z"/></svg>
        peter@tideharborfinance.com.au
      </li>
    </ul>
  </section>

  <section class="card card-back" aria-label="Business card back">
    <div class="back-brand">
      <div class="brand-mark"></div>
      <div class="brand-name">Tide<br>Harbor<br>Finance</div>
    </div>
    <p class="slogan">Steady guidance, secure futures</p>
    <h2 class="services-heading">
      <svg class="arrow" viewBox="0 0 12 12"><path d="M0 6 12 0v12z"/></svg>
      <span>Services <span class="accent">Offered</span></span>
      <svg class="arrow" viewBox="0 0 12 12"><path d="M12 6 0 0v12z"/></svg>
    </h2>
    <ul class="services-list">
      <li class="service">Home Loans</li>
      <li class="service">Investment Loans</li>
      <li class="service">First Home buyers</li>
      <li class="service row-start">Refinancing</li>
      <li class="service">Car Finance</li>
    </ul>
  </section>
</body>
</html>
```